Harbor Crest Homes Marketing Materials
2 Pocket Folder, Wine Label, Letterhead, Biz Card
Creative Brief
Professional
Derek "Rook" Abernathy
Chief Executive Officer
4872 Pellston Ave Unit C Brenholt, OR 46719
tcalloway47@mailbryte.com
https://harborcresthomes.net/
Use the SILVER version of the logo
Logo Large in the center of black card, make it ready for foil or spot UV

```html
<!DOCTYPE html>
<html lang="en">
<head>
<meta charset="utf-8">
<title>Harbor Crest Homes – Business Card</title>
<link href="https://fonts.googleapis.com/css2?family=Cinzel:wght@400;600&display=swap" rel="stylesheet">
<style>
  :root {
    --backdrop: #e6e6e8;
    --card: #2a2a2d;
    --card-edge: #1f1f22;
    --silver: #c9cacd;
    --silver-light: #eeeef0;
    --silver-mid: #9a9ba0;
    --text: #d6d7da;
  }
  * { margin: 0; padding: 0; box-sizing: border-box; }
  html, body { width: 1200px; height: 802px; overflow: hidden; }
  body {
    background: var(--backdrop);
    font-family: "Cinzel", "Times New Roman", serif;
    position: relative;
  }
  .card {
    position: absolute;
    top: 252px;
    width: 520px;
    height: 298px;
    background: var(--card);
    border-radius: 3px;
    overflow: hidden;
    box-shadow: 0 6px 18px rgba(0,0,0,0.18);
  }
  .card--back { left: 60px; }
  .card--front { left: 620px; }

  /* Back: details side */
  .swoosh { position: absolute; left: 0; bottom: 0; width: 520px; height: 120px; }
  .back-mark {
    position: absolute;
    left: 30px; top: 92px;
    width: 220px;
    text-align: center;
    color: var(--silver);
    font-weight: 600;
    font-size: 28px;
    line-height: 1.1;
    letter-spacing: 1px;
    text-transform: uppercase;
  }
  .divider {
    position: absolute;
    left: 268px; top: 34px;
    width: 1px; height: 170px;
    background: var(--silver-mid);
  }
  .details {
    position: absolute;
    left: 286px; top: 36px;
    width: 220px;
    color: var(--text);
    font-size: 11px;
    line-height: 1.65;
    letter-spacing: 0.3px;
  }
  .details .name { font-size: 12.5px; text-transform: uppercase; font-weight: 600; letter-spacing: 0.6px; }
  .details .title { margin-bottom: 10px; }
  .details .address { margin-bottom: 10px; }
  .contact { display: flex; align-items: center; gap: 6px; }
  .contact svg { width: 10px; height: 10px; flex: none; }

  /* Front: logo side */
  .front-mark {
    position: absolute;
    inset: 0;
    display: flex;
    align-items: center;
    justify-content: center;
    text-align: center;
    color: var(--silver);
    font-weight: 600;
    font-size: 44px;
    line-height: 1.1;
    letter-spacing: 2px;
    text-transform: uppercase;
  }
</style>
</head>
<body>
  <section class="card card--back" aria-label="Business card back">
    <div class="back-mark">Harbor Crest<br>Homes</div>
    <div class="divider"></div>
    <div class="details">
      <div class="name">Derek "Rook" Abernathy</div>
      <div class="title">Chief Executive Officer</div>
      <div class="address">4872 Pellston Ave<br>Unit C Brenholt, OR 46719</div>
      <div class="contact">
        <svg viewBox="0 0 10 10"><path d="M2 1l2 2-1 1.2c.6 1.2 1.6 2.2 2.8 2.8L7 6l2 2-1.3 1.3C4.5 9 1 5.5.7 2.3z" fill="var(--text)"/></svg>
        <span>219-555-0173</span>
      </div>
      <div class="contact">
        <svg viewBox="0 0 10 10"><rect x="0.5" y="2" width="9" height="6" fill="none" stroke="var(--text)"/><path d="M0.5 2l4.5 3.5L9.5 2" fill="none" stroke="var(--text)"/></svg>
        <span>tcalloway47@mailbryte.com</span>
      </div>
      <div class="contact">
        <svg viewBox="0 0 10 10"><circle cx="5" cy="5" r="4.3" fill="none" stroke="var(--text)"/><path d="M0.7 5h8.6M5 0.7c-2 2.5-2 6.1 0 8.6M5 0.7c2 2.5 2 6.1 0 8.6" fill="none" stroke="var(--text)" stroke-width="0.7"/></svg>
        <span>harborcresthomes.net</span>
      </div>
    </div>
    <svg class="swoosh" viewBox="0 0 520 120" preserveAspectRatio="none" aria-hidden="true">
      <path d="M0 70 C140 40 300 120 520 60 L520 120 L0 120 Z" fill="var(--silver-mid)"/>
      <path d="M0 82 C150 55 300 128 520 74 L520 120 L0 120 Z" fill="var(--silver-light)"/>
      <path d="M0 96 C160 74 310 132 520 92 L520 120 L0 120 Z" fill="var(--card-edge)"/>
    </svg>
  </section>

  <section class="card card--front" aria-label="Business card front">
    <div class="front-mark">Harbor Crest<br>Homes</div>
  </section>
</body>
</html>
```